Patient Fact sheets for medical conditions and treatments

Hi,

I need a new design for my patient fact sheets. I am moving from my current clinic and I am looking from a new look.

I have attached
1. a current Fact sheet
2. New home page to the website
3. New Logo.

They need to be single page and easily readable for patients.

The will be in both PDF and print form in the future.

Target Market(s)

Patients with chronic pain age 40+

Font styles to use
Serif

Requirements
Must have
• My logo, should be inline with design elements on the Front page provided.

Please use the same font as the Logo

```html
<!DOCTYPE html>
<html lang="en">
<head>
<meta charset="utf-8">
<title>PRP Therapy Fact Sheet</title>
<link href="https://fonts.googleapis.com/css2?family=Cinzel:wght@400&family=Open+Sans:wght@400&display=swap" rel="stylesheet">
<style>
:root{
  --bg:#ebe8e3;
  --paper:#ffffff;
  --band:#d5d5d9;
  --panel:#f1f1f2;
  --ink:#2a2a2e;
  --text:#3c3c40;
  --navy:#262660;
  --bullet:#a9a9b8;
  --icon:#2c2c5e;
  --social:#3b7bbf;
}
*{margin:0;padding:0;box-sizing:border-box}
html,body{width:1200px;height:882px;overflow:hidden;background:var(--bg)}
body{position:relative;font-family:"Open Sans",Arial,sans-serif;color:var(--text)}
.sheet{position:absolute;top:38px;width:553px;height:781px;background:var(--paper);box-shadow:0 2px 8px rgba(0,0,0,.25)}
.sheet--front{left:30px}
.sheet--back{left:618px}
.abs{position:absolute}

.practice-name{position:absolute;left:37px;top:74px;display:flex;align-items:center;gap:9px;font-family:"Open Sans",Arial,sans-serif;font-weight:400;color:var(--ink);font-size:19px;line-height:24px;white-space:nowrap}
.practice-name__mark{width:9px;height:9px;background:var(--ink)}
.practice-name--small{left:147px;top:562px;font-size:10px;line-height:12px;gap:0}

.title-band{position:absolute;left:256px;top:49px;width:297px;height:76px;background:var(--band);display:flex;align-items:center;justify-content:center;font-family:"Cinzel",Georgia,serif;color:#fff;font-size:40px;letter-spacing:1px}

.photo{position:absolute}
.photo--lab{left:0;top:175px;width:322px;height:192px;background:linear-gradient(100deg,#cfd3d6 0%,#eef0f1 35%,#e7c23a 55%,#f3d35a 62%,#dfe2e4 80%,#c7cbce 100%)}
.intro{position:absolute;left:322px;top:175px;width:231px;height:192px;background:var(--panel);padding:8px 20px 0 30px}
.intro h1{font-family:"Cinzel",Georgia,serif;font-weight:400;font-size:15px;line-height:18px;text-align:center;color:var(--ink);margin-bottom:12px}
.body-copy{font-size:8.4px;line-height:11.2px}

h2{font-family:"Cinzel",Georgia,serif;font-weight:400;color:var(--ink);font-size:13.5px;line-height:18px;letter-spacing:.2px}
.col{position:absolute;font-size:8.2px;line-height:13px}
.col--one{left:48px;top:429px;width:142px}
.col--two{left:219px;top:426px;width:145px}
.col--three{left:387px;width:145px;line-height:11.2px}

.bullets{list-style:none}
.bullets li{position:relative;padding-left:14px}
.bullets li::before{content:"";position:absolute;left:1px;top:4px;width:4px;height:4px;background:var(--bullet);transform:rotate(45deg)}
.col--three .bullets li{margin-bottom:5px}

.scan{position:absolute;top:700px;height:78px}
.scan--a{left:4px;width:181px;background:radial-gradient(ellipse at 50% 40%,#3a3a3a 0%,#8a8a8a 45%,#d2d2d2 100%)}
.scan--b{left:187px;width:179px;background:linear-gradient(90deg,#111 0%,#6c6c6c 30%,#2a2a2a 55%,#8e8e8e 75%,#1a1a1a 100%)}
.scan--c{left:370px;width:180px;background:linear-gradient(120deg,#5c5c5c 0%,#b9b9b9 45%,#d9d9d9 70%,#9b9b9b 100%)}

.treat{position:absolute;left:38px;top:188px;width:200px}
.treat .lead{margin:16px 0 0 23px;font-size:8.4px}
.treat .bullets{margin:20px 0 0 23px;font-size:8.4px;line-height:15.8px}
.treat .bullets li::before{top:6px}
.treat .note{margin:14px 0 0 23px;width:140px;font-size:8.4px;line-height:12.8px}

.results{position:absolute;left:242px;top:175px;width:311px;height:275px;background:var(--panel)}
.results h2{position:absolute;left:18px;top:9px;font-size:13px;white-space:nowrap}
.results p{position:absolute;left:50px;top:62px;width:220px;font-size:8.4px;line-height:15.7px}

.info-band{position:absolute;left:-3px;top:508px;width:556px;height:24px;background:var(--navy);color:#fff;font-family:"Cinzel",Georgia,serif;font-size:11.5px;line-height:24px;text-align:center;letter-spacing:.3px}
.portrait{position:absolute;left:40px;top:559px;width:90px;height:121px;background:linear-gradient(160deg,#e6e6e6 0%,#9a9a9a 45%,#2a2a2a 80%,#4a4a4a 100%)}
.contact{position:absolute;font-size:8.6px;line-height:11.5px;color:var(--ink)}
.contact--address{left:160px;top:637px}
.contact--phone{left:273px;top:641px;font-size:10px;line-height:12px}
.contact--web{left:355px;top:641px;width:130px;text-align:center}
.icon{position:absolute}
.social{position:absolute;left:506px;width:12px;height:12px;background:var(--social)}

.disclaimer{position:absolute;left:40px;top:705px;width:482px;color:#111}
.disclaimer h3{font-weight:400;font-size:6px;margin-bottom:8px}
.disclaimer p{font-size:5.6px;line-height:7.8px}
</style>
</head>
<body>

<section class="sheet sheet--front">
  <div class="practice-name"><span class="practice-name__mark"></span>Dr Ian Hale</div>
  <div class="title-band">FACT SHEET</div>

  <div class="photo photo--lab" role="img" aria-label="Gloved hand holding test tubes of yellow plasma"></div>
  <div class="intro">
    <h1>Platelet Rich Plasma<br>(PRP) Therapy</h1>
    <p class="body-copy">Platelet-Rich Plasma (PRP) is concentrated platelets and white blood cells derived from your own blood. Platelet Rich Plasm Injection Therapy (PRP therapy), is a growing treatment approach for soft tissue injuries including tendon, muscle and ligaments. It is also showing good results for mild to moderate osteoarthritis. While this approach has been used overseas for many years, it's fairly new to Australia in the treatment of musculoskeletal and orthopaedic conditions.</p>
  </div>

  <h2 class="abs" style="left:48px;top:398px">How does PRP work?</h2>
  <div class="col col--one">Some tissues in the body have a poor blood supply or respond poorly to excessive load, ultimately failing to heal naturally. While some of our primary treatment such as physiotherapy, massage, biomechanical correction and other forms of treatment are used to treat these soft tissue injuries, sometimes the body fails to respond. PRP therapy utilises the healing properties in blood to allow a healing reaction to occur in a tissue that's not healing on its own. Our blood has small granules called 'platelets', which contain special growth factors that when released, allow stem cells in the particular tissue to 'switch' on and cause new</div>
  <div class="col col--two">tissue to be created and heal the injured area.<br>Take the example of achilles tendinopathy. If the achilles is painful, thickened and not responding to rehabilitation, then the sports physician will inject the PRP into the achilles which will cause the tendon cells (tenocytes/fibroblasts) to create new achilles collagen to strengthen the achilles. White blood cells also enter the area to mop up any achilles tissue that may have been damaged due to the ongoing pain and thickening in the area.</div>

  <h2 class="abs" style="left:384px;top:390px">Role of Platelets &amp;<br>Growth Factors</h2>
  <div class="col col--three" style="top:438px;line-height:13px">PRP contains highly concentrated platelets. Platelets have been identified to secrete growth factors, which are known to play a role in:</div>
  <div class="col col--three" style="top:498px;left:403px;width:130px">
    <ul class="bullets">
      <li>increasing tissue vascularity and increasing the rate of epithelial tissue production (wound healing)</li>
      <li>attracting other cells that fight infection</li>
      <li>acting as a seal during closures</li>
      <li>providing an immediate surgical hemostatic agent (reduction of bleeding)</li>
      <li>osteogenesis (bone regeneration and repair)</li>
    </ul>
  </div>

  <div class="scan scan--a" role="img" aria-label="X-ray image of the spine"></div>
  <div class="scan scan--b" role="img" aria-label="MRI scan of the spine"></div>
  <div class="scan scan--c" role="img" aria-label="X-ray image of a joint"></div>
</section>

<section class="sheet sheet--back">
  <div class="practice-name"><span class="practice-name__mark"></span>Dr Ian Hale</div>
  <div class="title-band">FACT SHEET</div>

  <div class="treat">
    <h2>What can PRP treat?</h2>
    <p class="lead">PRP therapy can be used for:</p>
    <ul class="bullets">
      <li>orthopedic surgery</li>
      <li>cardiac surgery</li>
      <li>plastic and cosmetic surgery</li>
      <li>ear, nose, throat (ENT) surgery</li>
      <li>oral maxillofacial surgery</li>
      <li>neurosurgery</li>
      <li>vascular surgery</li>
      <li>wound healing</li>
      <li>burn care.</li>
    </ul>
    <p class="note">Ask your doctor whether plateletrich plasma is appropriate for your surgical procedur</p>
  </div>

  <div class="results">
    <h2>What are the expected results of PRP?</h2>
    <p>Because the goal of PRP therapy is to resolve pain through healing, it could prove to have lasting results. Initial improvement may be seen within a few weeks, gradually increasing as the healing progresses. Research studies and clinical practice have shown PRP therapy to be very effective at relieving pain and returning patients to their normal lives. The need for surgery can also be greatly reduced by treating injured tissues before the damage progresses and the condition is irreversible.</p>
  </div>

  <div class="info-band">For more information</div>
  <div class="portrait" role="img" aria-label="Portrait photograph of the doctor"></div>
  <div class="practice-name practice-name--small">Dr Ian Hale</div>

  <svg class="icon" style="left:186px;top:605px" width="12" height="17" viewBox="0 0 12 17"><path d="M6 0C2.7 0 0 2.6 0 5.9 0 10.2 6 17 6 17s6-6.8 6-11.1C12 2.6 9.3 0 6 0z" fill="var(--icon)"/><circle cx="6" cy="6" r="2.2" fill="#fff"/></svg>
  <div class="contact contact--address">Elm House,<br>Ground Floor<br>48 Harlow Road<br>Ferndale VIC 3999</div>

  <svg class="icon" style="left:291px;top:604px" width="26" height="22" viewBox="0 0 26 22"><rect x="2" y="2" width="12" height="18" rx="1.5" fill="none" stroke="var(--icon)" stroke-width="2"/><rect x="9" y="9" width="15" height="11" fill="#fff" stroke="var(--icon)" stroke-width="2"/><path d="M9 9l7.5 6L24 9" fill="none" stroke="var(--icon)" stroke-width="2"/></svg>
  <div class="contact contact--phone">03 9000 4111<br>03 9000 4110</div>

  <svg class="icon" style="left:407px;top:600px" width="24" height="24" viewBox="0 0 24 24" fill="none" stroke="var(--icon)" stroke-width="2"><circle cx="11" cy="11" r="9"/><ellipse cx="11" cy="11" rx="4" ry="9"/><path d="M2 11h18M4 6h14M4 16h14"/><path d="M15 14l7 3-3 1-1 3z" fill="var(--icon)"/></svg>
  <div class="contact contact--web">info@northgatepain.example<br>northgatepain.example</div>

  <div class="social" style="top:599px"></div>
  <div class="social" style="top:618px"></div>
  <div class="social" style="top:637px"></div>

  <div class="disclaimer">
    <h3>DISCLAIMER</h3>
    <p>Please note the contents of this patient fact sheet are general information only and are not a substitute for advice from your own health professional about diagnosis or treatment. At Northgate Pain Group each patient's condition is assessed individually, and recommended treatments and their outcomes will vary from person to person. To find out whether a treatment suits your condition, please speak with one of our doctors at your consultation.</p>
  </div>
</section>

</body>
</html>
```